Forest Consultant/Timber Buyer needs a clean business card

We are a forestry consulting and timber buying company. We meet with private landowners and assist them with timber management and timber harvesting. We would like a professional business card, please no clip art. logo is blue and white but would like to see a gray,silver, or some other color incorporated. Would like basic contact info. Would like to the layout to be creative and sleek but masculine.

Target Market(s)

private landowners

Industry/Entity Type

Business

Contact Information for Business Card

name,position, cell number, office number, email, website. This might be to cluttered. Basic contact info is what we are looking for.

Contact info can all be on one side with logo on the other.

Font styles to use
Serif
Sans Serif

Colors
0255a3
ffffff
aaaaaa

Requirements
Must have
• We just want it professional.
Nice to have
• Creative layout.
Should not have
• please no clip art of log trucks etc.

```html
<!DOCTYPE html>
<html lang="en">
<head>
<meta charset="utf-8">
<title>Oakridge Land &amp; Timber — Business Card</title>
<link href="https://fonts.googleapis.com/css2?family=PT+Sans:wght@400;700&display=swap" rel="stylesheet">
<style>
  :root {
    --brand-blue: #0255a3;
    --white: #ffffff;
    --silver: #aaaaaa;
    --card-black: #0d0d0d;
    --card-edge: #1c1c1c;
    --backdrop: #b9b9b9;
  }
  * { margin: 0; padding: 0; box-sizing: border-box; }
  html, body {
    width: 1200px;
    height: 900px;
    overflow: hidden;
    background: var(--backdrop);
    font-family: "PT Sans", sans-serif;
  }
  .canvas {
    width: 1200px;
    height: 900px;
    display: flex;
    flex-direction: column;
    align-items: center;
    justify-content: center;
    gap: 44px;
  }
  .card {
    position: relative;
    width: 700px;
    height: 400px;
    background: radial-gradient(ellipse at 55% 35%, var(--card-edge) 0%, var(--card-black) 70%);
    box-shadow: 0 6px 18px rgba(0,0,0,.25);
    color: var(--white);
  }
  /* Front side: company name centred */
  .card--front {
    height: 370px;
    display: flex;
    align-items: center;
    justify-content: center;
  }
  .brand {
    display: flex;
    align-items: center;
    gap: 18px;
  }
  .brand__dot {
    width: 22px;
    height: 22px;
    border-radius: 50%;
    background: currentColor;
  }
  .brand__name {
    font-weight: 700;
    font-size: 42px;
    letter-spacing: 3px;
    text-transform: uppercase;
    line-height: 1;
  }
  .card--front .brand { color: var(--white); }

  /* Back side: contact details */
  .card--back { height: 370px; }
  .card--back .brand {
    position: absolute;
    top: 70px;
    right: 50px;
    color: var(--brand-blue);
  }
  .card--back .brand__name { font-size: 30px; letter-spacing: 2px; }
  .person {
    position: absolute;
    top: 150px;
    left: 48px;
  }
  .person__name {
    color: var(--brand-blue);
    font-weight: 700;
    font-size: 20px;
  }
  .person__role {
    color: var(--white);
    font-size: 16px;
    margin-top: 2px;
  }
  .contact {
    position: absolute;
    right: 48px;
    bottom: 44px;
    list-style: none;
    text-align: right;
  }
  .contact__item {
    display: flex;
    align-items: center;
    justify-content: flex-end;
    gap: 12px;
    font-size: 18px;
    line-height: 26px;
    color: var(--white);
  }
  .contact__icon {
    width: 14px;
    height: 14px;
    fill: none;
    stroke: var(--brand-blue);
    stroke-width: 2;
  }
  .contact__icon--solid { fill: var(--brand-blue); stroke: none; }
</style>
</head>
<body>
<main class="canvas">
  <section class="card card--front" aria-label="Card front">
    <div class="brand">
      <span class="brand__dot"></span>
      <span class="brand__name">Oakridge Land &amp; Timber</span>
    </div>
  </section>

  <section class="card card--back" aria-label="Card back">
    <div class="brand">
      <span class="brand__dot"></span>
      <span class="brand__name">Oakridge Land &amp; Timber</span>
    </div>

    <div class="person">
      <p class="person__name">Daniel Carter</p>
      <p class="person__role">Managing Director</p>
    </div>

    <ul class="contact">
      <li class="contact__item">044-555 018 274
        <svg class="contact__icon" viewBox="0 0 14 14"><rect x="4" y="1" width="6" height="12" rx="1"/></svg>
      </li>
      <li class="contact__item">044-555 018 274
        <svg class="contact__icon contact__icon--solid" viewBox="0 0 14 14"><path d="M3 1l3 3-1.5 1.5c.8 1.8 2.2 3.2 4 4L10 8l3 3-2 2C6 13 1 8 1 3z"/></svg>
      </li>
      <li class="contact__item">info@oakridgetimber.com
        <svg class="contact__icon contact__icon--solid" viewBox="0 0 14 14"><path d="M1 3h12v8H1z"/><path d="M1 3l6 5 6-5" stroke="#0d0d0d" stroke-width="1.2" fill="none"/></svg>
      </li>
      <li class="contact__item">www.oakridgetimber.com
        <svg class="contact__icon contact__icon--solid" viewBox="0 0 14 14"><circle cx="7" cy="7" r="6"/><path d="M1 7h12M7 1c-3 3-3 9 0 12M7 1c3 3 3 9 0 12" stroke="#0d0d0d" stroke-width="1" fill="none"/></svg>
      </li>
    </ul>
  </section>
</main>
</body>
</html>
```